IT Distribution Wholesale Business Card & Logo Design

I need both logo and a business card that suits our business model, am happy to pay more for great effort put in.
Brevon Orbital Australia Pty Ltd
An IT Distribution / Wholesale company that distributes technology hardwares, softwares, components, etc.
Offer drop ship services for online retailers and supply to Australia-wide.
Based in Sydney Australia.
Design should give impressions of trust and stability.

Slogan: "your one stop technology supplier"
*two-sided name card
*logo + slogan on the back of the card

I don't have much specific requirements, leave it to designers to come up with creative & interesting masterpiece.
The logo and business card comes in first which i would like it to be completed latest by mid of March, we will require a whole redesign of our web pages, banner design, catalogue design later part.

Goodluck & thank you for your effort.

Hello designers,

Busy week, very good return rate on the number of designs and effort put into our business card design.
I thank you all for that.
We will have to extend this project for another week to two to receive more designs and more time for me to post some updates to you all.
We are getting there, i really liked some of the designs sent but just not the perfect masterpiece we are looking for.

Cheers,
Darnell Q.

Target Market(s)

Computer Retailers, Corporate, Schools, Councils.

Industry/Entity Type

Business

Requirements
Must have
• Brevon Orbital (Australia) Pty Ltd, Darnell Quist, Managing Director, Unit C, 14-18 Pellham Road, Dunmore NSW 2461, Ph +61 2 5037 1942, M +61 4 70395216, E darnell@brevonorbital.com.au, W www.brevonorbital.com.au
Nice to have
• Keep it simple & comfortable.
Target audiences are mostly >30-40 years old range.

Example of companies in the same line:-
http://www.kzp.com.au
http://www.norvix.com.au/
http://www.supplyhaventrade.com/
http://www.quenby.com.au/
http://www.bq456.com.au/
https://www.swiftgridhub.com.au/
http://carvelo.com.au/

```html
<!DOCTYPE html>
<html lang="en">
<head>
<meta charset="UTF-8">
<title>Brevon Orbital – Card Back</title>
<link href="https://fonts.googleapis.com/css2?family=Lato:ital,wght@0,300;1,300&display=swap" rel="stylesheet">
<style>
  :root {
    --card-bg: #231f20;
    --brand-red: #c72035;
    --slogan-red: #c23a48;
  }
  html, body {
    margin: 0;
    padding: 0;
    overflow: hidden;
    background: var(--card-bg);
  }
  .card-back {
    position: relative;
    width: 741px;
    height: 1200px;
    background: var(--card-bg);
    overflow: hidden;
  }
  .slogan {
    position: absolute;
    left: 87px;
    top: 342px;
    margin: 0;
    font-family: "Lato", sans-serif;
    font-style: italic;
    font-weight: 300;
    font-size: 26px;
    line-height: 1.2;
    letter-spacing: 1.25px;
    color: var(--slogan-red);
    white-space: nowrap;
  }
  .brand-mark {
    position: absolute;
    left: 243px;
    top: 400px;
    width: 498px;
    height: 300px;
    display: flex;
    align-items: center;
    justify-content: center;
    gap: 30px;
  }
  .brand-dot {
    width: 170px;
    height: 170px;
    border-radius: 50%;
    background: var(--brand-red);
    flex: none;
  }
  .brand-name {
    font-family: "Lato", sans-serif;
    font-weight: 300;
    font-size: 66px;
    line-height: 1.05;
    color: var(--brand-red);
    white-space: nowrap;
  }
</style>
</head>
<body>
  <main class="card-back">
    <p class="slogan">your one stop technology supplier</p>
    <div class="brand-mark">
      <span class="brand-dot"></span>
      <span class="brand-name">Brevon<br>Orbital</span>
    </div>
  </main>
</body>
</html>
```